Hollowmere Yuletide Firs needs words putting into pictures!

Hollowmere Yuletide Firs sells real Christmas Trees directly to consumers and retailers. A "growing" part of our business is fulfilling online orders e.g. a garden centre sells a tree online, and we do everything else from selecting the tree to delivery. We are now looking to market this service as best in class due to the selection process we have, and a link up we have made with a courier company.

We want to summarise the process into a simple one page graphic that illustrates the process from start to finish in simple language, short sentences, with images and pictures.

Given how difficult it is to get good images of Christmas trees, we thought simple outline pictures could work - almost like sketches. We are open to all ideas.

We can provide any of the images in the attached brochure, and many more depending what you may require.

We like clean cut, simple designs that are clear and innovative.

Contact Information for Business Card

Simon Carver, Director, Hollowmere Yuletide Firs, simon@hollowmereyuletidefirs.example, Brackwell Croft Farm, Brackwell Croft Lane, Thistleby Moor, QX4 8TD

Font styles to use
Sans Serif

Colors
00a990

Requirements
Must have
• Condense the info down into a manageable graphic that shows our customers clearly what service we are able to provide
Nice to have
• Simple, elegant design to compliment brand feel
Should not have
• Not be too complicated

```html
<!DOCTYPE html>
<html lang="en">
<head>
<meta charset="utf-8">
<title>Hollowmere Yuletide Firs – Online Delivery Service</title>
<link rel="stylesheet" href="https://fonts.googleapis.com/css2?family=Lato:ital,wght@0,400;0,700;1,400&display=swap">
<style>
  :root {
    --ink: #222222;
    --brand-navy: #3a3a78;
    --brand-green: #3f8f3a;
    --leaf-light: #b9d98e;
    --leaf-mid: #6db33f;
    --leaf-dark: #2f7d32;
    --art-a: #e4f0d8;
    --art-b: #c9e2ae;
    --rule: #555555;
    --frame: #333333;
    --canvas: #ffffff;
  }
  * { margin: 0; padding: 0; box-sizing: border-box; }
  html, body { width: 1200px; height: 900px; overflow: hidden; background: var(--canvas); }
  body { position: relative; font-family: "Lato", sans-serif; color: var(--ink); }

  .sheet { position: absolute; top: 93px; height: 705px; border: 1px solid var(--frame); background: var(--canvas); }
  .sheet--process { left: 40px; width: 544px; }
  .sheet--about { left: 615px; width: 545px; }

  .brand { position: absolute; text-align: center; top: 30px; }
  .brand__mark { display: block; margin: 0 auto 8px; width: 14px; height: 14px; border-radius: 50%; background: var(--brand-green); }
  .brand__name { font-weight: 700; font-size: 17px; line-height: 1.15; color: var(--brand-navy); letter-spacing: .5px; }
  .sheet--process .brand { left: 40px; width: 194px; }
  .sheet--about .brand { left: 172px; width: 200px; }

  .sheet-title { position: absolute; font-weight: 400; color: var(--ink); text-align: center; }
  .sheet--process .sheet-title { left: 25px; top: 168px; width: 244px; font-size: 14px; }
  .sheet--about .sheet-title { left: 0; top: 190px; width: 100%; font-size: 15px; }

  .column-rule { position: absolute; left: 271px; top: 77px; width: 1px; height: 538px; background: var(--rule); }

  .step-art { position: absolute; border-radius: 4px; background: linear-gradient(135deg, var(--art-a), var(--art-b)); }
  .step-art--1 { left: 25px; top: 196px; width: 95px; height: 36px; }
  .step-art--2 { left: 38px; top: 290px; width: 65px; height: 40px; }
  .step-art--3 { left: 30px; top: 380px; width: 85px; height: 40px; }
  .step-art--4 { left: 38px; top: 500px; width: 75px; height: 78px; }
  .step-art--5 { left: 322px; top: 70px; width: 55px; height: 88px; }
  .step-art--6 { left: 332px; top: 228px; width: 60px; height: 70px; }
  .step-art--7 { left: 300px; top: 392px; width: 82px; height: 75px; }
  .step-art--8 { left: 300px; top: 518px; width: 90px; height: 62px; }

  .step { position: absolute; font-size: 10px; line-height: 13.5px; }
  .step::before { content: ""; float: left; width: 105px; height: 40px; }
  .step__num { color: var(--brand-green); font-weight: 700; }
  .step p + p { margin-top: 13px; }

  .step--1, .step--2, .step--3, .step--4 { left: 25px; width: 245px; }
  .step--5, .step--6, .step--7, .step--8 { left: 290px; width: 230px; }
  .step--5::before, .step--6::before, .step--7::before, .step--8::before { width: 103px; }
  .step--1 { top: 204px; }
  .step--2 { top: 297px; }
  .step--3 { top: 393px; }
  .step--4 { top: 536px; }
  .step--5 { top: 115px; }
  .step--6 { top: 255px; }
  .step--7 { top: 429px; }
  .step--8 { top: 539px; }

  .contact { position: absolute; left: 0; top: 648px; width: 100%; text-align: center; font-size: 10px; line-height: 13px; color: var(--brand-green); font-style: normal; }

  .benefits { position: absolute; left: 0; top: 213px; width: 100%; list-style: none; text-align: center; font-size: 10px; line-height: 13px; }
  .benefits li::before { content: "• "; }
  .benefits em { font-style: italic; }

  .banner { position: absolute; left: 30px; top: 270px; width: 488px; height: 86px;
    background: linear-gradient(180deg, var(--leaf-light) 0%, var(--leaf-mid) 55%, var(--leaf-dark) 100%); }

  .story { position: absolute; left: 30px; top: 366px; width: 488px; font-size: 10px; line-height: 13.2px; text-align: justify; letter-spacing: -0.1px; }
  .story p + p { margin-top: 11px; }
</style>
</head>
<body>

<section class="sheet sheet--process">
  <div class="brand">
    <span class="brand__mark"></span>
    <div class="brand__name">HOLLOWMERE<br>YULETIDE FIRS</div>
  </div>
  <h1 class="sheet-title">Online Delivery Service</h1>

  <div class="step-art step-art--1" role="img" aria-label="Outline sketch of hills and plantation fields in Scotland"></div>
  <div class="step-art step-art--2" role="img" aria-label="Outline sketch of three trees with one selected by a tick"></div>
  <div class="step-art step-art--3" role="img" aria-label="Outline sketch of a truck carrying a cut tree"></div>
  <div class="step-art step-art--4" role="img" aria-label="Outline sketch of a tree with height and width measures and a tick"></div>
  <div class="step-art step-art--5" role="img" aria-label="Outline sketch of a netted tree with a label tag"></div>
  <div class="step-art step-art--6" role="img" aria-label="Outline sketch of a freshly cut tree trunk end"></div>
  <div class="step-art step-art--7" role="img" aria-label="Outline sketch of a computer, phone and clock"></div>
  <div class="step-art step-art--8" role="img" aria-label="Outline sketch of a tree beside a December calendar"></div>

  <div class="step step--1">
    <p><span class="step__num">1.</span> We view the trees several times per year in Scotland, and choose which fields and plantations our trees will be cut from.</p>
  </div>
  <div class="step step--2">
    <p><span class="step__num">2.</span> We choose specific premium quality trees and label them in the field in September time to ensure our customers receive only the very best trees.</p>
  </div>
  <div class="step step--3">
    <p><span class="step__num">3.</span> The trees are cut between the end of November and mid December, depending upon the proposed delivery date. They are transported to a farm where they are measured and graded for a second time. the trunk is cut and placed in water so that the tree can begin drinking again.</p>
  </div>
  <div class="step step--4">
    <p><span class="step__num">4.</span> Every tree is hand picked for each customer. Two days before the delivery date, the tree is selected and checked for a third time to make sure that it meets the size and quality specifications, and any special requests which have been made.</p>
  </div>

  <div class="column-rule"></div>

  <div class="step step--5">
    <p><span class="step__num">5.</span> The tree is then labelled for the customer and netted through a Christmas tree netting funnel to make it easier to handle and transport. Packaged in a special tree transport bag, full protection for the tree is provided.</p>
  </div>
  <div class="step step--6">
    <p><span class="step__num">6.</span> As close as possible to dispatch 2cm is chopped off the bottom of the tree - this opens the tree up and means it is more likely to drink water when in a water holding stand.</p>
    <p>The tree is dispatched the working day before it is due for delivery to keep the time spent in transit to a minimum and maximise freshness.</p>
  </div>
  <div class="step step--7">
    <p><span class="step__num">7.</span> The customer receives texts/emails throughout the day of their delivery to update on the progress of the driver. If possible, the driver will call 30 mins before delivery</p>
  </div>
  <div class="step step--8">
    <p><span class="step__num">8.</span> Trees are cut at regular intervals throughout December to ensure that we constantly have a fresh supply of Christmas trees, and to reduce the time between the tree being cut, and it being delivered to the customer.</p>
  </div>

  <address class="contact">sales@hollowmereyuletidefirs.example<br>www.hollowmereyuletidefirs.example</address>
</section>

<section class="sheet sheet--about">
  <div class="brand">
    <span class="brand__mark"></span>
    <div class="brand__name">HOLLOWMERE<br>YULETIDE FIRS</div>
  </div>
  <h2 class="sheet-title">Why Choose Us?</h2>
  <ul class="benefits">
    <li>Full customer service support</li>
    <li>Efficient transport - <em>Monday to Sunday Delivery</em></li>
    <li>Damage prevention - <em>Bespoke tree transport bag (branded)</em></li>
    <li>Careful selection with multiple stages of quality control where the Trees are Grown</li>
  </ul>

  <div class="banner" role="img" aria-label="Illustrated banner of rolling green fields and a row of fir trees"></div>

  <div class="story">
    <p>Every tree has a story. Each plantation and field we harvest trees from has specific characteristics that display in the trees. A number of factors affect this – the location of the forest and local weather conditions, the type and composition of the soil, the type and provenance of seedlings used and the specialist skills of each grower.</p>
    <p>Each type of tree requires very careful management and growing premium quality Christmas trees is a skilled and rare profession.</p>
    <p>Our Nordmann fir trees (up to 8 feet) are grown on the edge of a small village hidden deep in the Scottish borders on a farm that has produced some of the best trees available each and every year. A dedicated team has perfected the art of nurturing the trees in their early years, before using a specialist hand pruning method to shape them into perfect specimens.</p>
    <p>Our Fraser Fir trees are grown on a rather inaccessible piece of land called Crannoch Rise in the heart of Scotland. Crannoch Rise is an area at the top of a hill with fantastic views and is only accessible on foot or by tractor – it is not a place you can stumble upon. This land has a rather unique composition, which makes inhospitable for most plant life, but ideal for Fraser Fir. Our larger trees are grown on two farms deep in the hills beyond Loch Lomond, and near the coast north of Fife. They are carefully tended to for over ten years using a range of special equipment to give a lovely shape. By using a combination of locations for our trees, we can rely on the specialisms of each grower, and provide a resilient and consistent supply. We can also be flexible with the harvest of the tree and adapt to the local weather conditions to make sure that the trees have had sufficient frost before being cut.</p>
  </div>

  <address class="contact">sales@hollowmereyuletidefirs.example<br>www.hollowmereyuletidefirs.example</address>
</section>

</body>
</html>
```